Football and Sports Management Agency Stationary

We have a logo, fonts, website and colour palette.
We need the logo refined by a proper designer and then business stationary designed. You can see on the website how it needs adjusting by a designers eye.
The company is a high end sports management company aiming to attract and represent professional athletes. The name Velorin is to indicate a 'Constellation of Stars' ie our clients. The dots on the star should be slightly different sizes to reflect that some clients will be bigger than others.
Colours:
#e6e6e6
#edd2a4
#caaa72 (main gold and also used on site)
#3f3f42
#001d38
#edeced (on website)
#191c23 (on website)
Font:
QT (velorin)
QT Melbrook (sports management)
We would like:
- Letterhead (word and indesign and PDF print format). I have attached an example for one I like. It's quiet a clean design with the contact details and address taking up only a small amount of room.
- Business card (dark on the back with the logo, personal details on the front). Only needs name, title, email, website and phone number. No company address (in PDF and indesign format)
- Powerpoint slide theme
- Logo in vector format for light and dark versions and single colour versions. And optimised web version
- Simple brand guide PDF showing colour, font and logo (a one/two page PDF)
Any questions, please ask.
NEW INFO:
Contact Details
Maren Solwick
Director
Mobile: +44 7630 218 977
Phone: +44 0113 872 604
Email: maren@velorinathletic.example
Web: velorinathletic.example
Corran Lodge, 14 Mill Bank Road, Stockport, SK4 9TW
Company number 40718362
Target Market(s)
Professional athletes, professional sports teams.
Industry/Entity Type
Management
Requirements
Must have
- NEW
- The designs must look cool, classy and high quality. My suggestion for this is to keep the text small and precise with uncomplicated design.
Nice to have
- Application of brand displayed on stationary and additional pieces of stationary branded.
- Draw some inspiration from the website. eg the slant angles used separate the sections.
Should not have
- Don't create new logos etc.

```html
<!DOCTYPE html>
<html lang="en">
<head>
<meta charset="utf-8">
<title>Velorin Sports Management – Stationery</title>
<link rel="stylesheet" href="https://fonts.googleapis.com/css2?family=Josefin+Sans:wght@300;400&family=Oswald:wght@400&display=swap">
<style>
  :root {
    --board: #474848;
    --navy: #1c1e27;
    --navy-deep: #15171e;
    --slide: #20222b;
    --gold: #caaa72;
    --gold-light: #edd2a4;
    --paper: #ffffff;
    --ink: #3f3f42;
    --mist: #e6e6e6;
  }
  * { box-sizing: border-box; margin: 0; padding: 0; }
  html, body { width: 1200px; height: 1200px; overflow: hidden; }
  body {
    background: var(--board);
    font-family: "Josefin Sans", Arial, sans-serif;
    position: relative;
  }
  .piece { position: absolute; overflow: hidden; box-shadow: 0 4px 10px rgba(0,0,0,.35); }
  .piece > svg.shape { position: absolute; inset: 0; }

  /* Wordmark */
  .wordmark { display: flex; align-items: center; font-weight: 300; text-transform: uppercase; white-space: nowrap; }
  .wordmark .dot { border-radius: 50%; background: var(--gold); flex: none; }
  .wordmark.on-light { color: var(--ink); }
  .wordmark.on-dark { color: var(--mist); }

  /* Letterhead */
  .letterhead { left: 52px; top: 78px; width: 475px; height: 673px; background: var(--paper); color: var(--ink); }
  .letterhead .wordmark { position: absolute; left: 62px; top: 102px; font-size: 14px; letter-spacing: 7px; }
  .letterhead .wordmark .dot { width: 6px; height: 6px; margin-right: 8px; }
  .letterhead .contact-list { position: absolute; left: 344px; top: 95px; font-size: 5.2px; line-height: 9px; list-style: none; }
  .contact-list li { display: flex; align-items: center; gap: 4px; }
  .contact-list svg { width: 5px; height: 5px; fill: var(--gold); }
  .letterhead .rule { position: absolute; left: 62px; top: 142px; width: 352px; height: 1px; background: var(--gold); }
  .letterhead .address { position: absolute; left: 62px; top: 177px; font-size: 7.3px; line-height: 9px; }
  .letterhead .date { position: absolute; left: 62px; top: 248px; font-size: 7.3px; }
  .letterhead .salutation { position: absolute; left: 62px; top: 304px; font-size: 7.3px; }
  .letterhead .body { position: absolute; left: 62px; top: 334px; width: 352px; font-size: 7.6px; line-height: 9.6px; text-align: justify; }
  .letterhead .body p { margin-bottom: 19px; }
  .letterhead .sender { position: absolute; left: 62px; top: 517px; font-size: 7.3px; }
  .letterhead .signature { position: absolute; left: 62px; top: 548px; width: 130px; height: 20px; background: linear-gradient(90deg, #d9dbe8, #eceef5); border-bottom: 1px solid #8a8fb5; }

  /* Business cards */
  .card { width: 290px; height: 165px; background: var(--navy); left: 494px; }
  .card-front { top: 246px; color: var(--gold); text-align: center; }
  .card-front .name { position: absolute; top: 43px; width: 100%; font-size: 7.5px; color: var(--mist); }
  .card-front .role { position: absolute; top: 55px; width: 100%; font-size: 6px; }
  .card-front .divider { position: absolute; left: 145px; top: 70px; width: 1px; height: 28px; background: var(--gold); }
  .card-front .col { position: absolute; top: 78px; font-size: 5.4px; line-height: 11px; list-style: none; }
  .card-front .col-left { right: 155px; text-align: right; }
  .card-front .col-right { left: 153px; text-align: left; }
  .card-front .col li { display: flex; align-items: center; gap: 3px; }
  .card-front .col-left li { justify-content: flex-end; }
  .card-front .col svg { width: 4.5px; height: 4.5px; fill: var(--gold); }
  .card-front .card-address { position: absolute; top: 109px; width: 100%; font-size: 5.4px; line-height: 7px; }
  .card-back { top: 427px; }
  .card-back .wordmark { position: absolute; top: 70px; left: 0; width: 100%; flex-direction: column; font-size: 20px; letter-spacing: 10px; padding-left: 10px; }
  .card-back .wordmark .dot { width: 7px; height: 7px; margin-bottom: 12px; margin-right: 10px; }

  /* Envelope */
  .envelope-back { left: 55px; top: 798px; width: 500px; height: 249px; background: var(--navy); }
  .envelope-back .wordmark { position: absolute; left: 0; width: 100%; top: 33px; justify-content: center; font-size: 14px; letter-spacing: 7px; }
  .envelope-back .wordmark .dot { width: 6px; height: 6px; margin-right: 9px; }
  .envelope-front { left: 270px; top: 910px; width: 500px; height: 249px; background: var(--navy); color: var(--mist); }
  .envelope-front .window { position: absolute; left: 38px; top: 94px; width: 168px; height: 84px; border-radius: 14px; background: linear-gradient(115deg, #f4f4f4 0%, #ffffff 45%, #d9d9d9 48%, #f2f2f2 60%, #ffffff 100%); }
  .envelope-front .wordmark { position: absolute; right: 40px; top: 70px; font-size: 17px; letter-spacing: 9px; }
  .envelope-front .wordmark .dot { width: 7px; height: 7px; margin-right: 12px; }
  .envelope-front .return-address { position: absolute; right: 28px; top: 141px; text-align: right; font-size: 7.4px; line-height: 11px; list-style: none; }
  .envelope-front .return-address .gap { margin-top: 3px; }

  /* Slides */
  .slide { left: 814px; width: 329px; height: 246px; background: var(--slide); color: var(--mist); }
  .slide-cover { top: 78px; }
  .slide-cover .stadium { position: absolute; inset: 0; background: radial-gradient(ellipse 70% 45% at 50% 62%, #31402f 0%, #1f2a24 45%, #15191c 100%); }
  .slide-cover .wordmark { position: absolute; left: 0; width: 100%; top: 110px; flex-direction: column; font-size: 24px; letter-spacing: 12px; padding-left: 12px; }
  .slide-cover .wordmark .dot { width: 8px; height: 8px; margin-bottom: 14px; margin-right: 12px; }
  .slide-title { position: absolute; left: 29px; top: 22px; font-family: "Oswald", "Arial Narrow", sans-serif; font-size: 17px; letter-spacing: .5px; color: #fff; }
  .slide-rule { position: absolute; left: 29px; top: 52px; width: 273px; height: 1px; background: var(--gold); }
  .slide .fine { font-size: 4.3px; line-height: 5.6px; color: #c9c9cc; text-align: justify; }
  .slide-footer-mark { position: absolute; left: 25px; bottom: 14px; font-size: 8px; letter-spacing: 4px; }
  .slide-footer-mark .dot { width: 4px; height: 4px; margin-right: 5px; }
  .slide-chart { top: 345px; }
  .slide-chart .copy { position: absolute; left: 29px; top: 73px; width: 125px; }
  .slide-chart svg.chart { position: absolute; left: 180px; top: 70px; width: 125px; height: 106px; }
  .slide-venn { top: 608px; }
  .slide-venn .note { position: absolute; width: 83px; font-size: 4.3px; line-height: 5.6px; color: #c9c9cc; }
  .slide-venn svg.venn { position: absolute; left: 110px; top: 75px; width: 108px; height: 110px; }
  .slide-media { top: 880px; }
  .slide-media .frame { position: absolute; left: 29px; top: 72px; width: 158px; height: 106px; border: 1px dashed #cfcfcf; display: flex; align-items: center; justify-content: center; }
  .slide-media .frame .placeholder { width: 40px; height: 32px; background: #e9ecf1; border: 1px solid #b9c0cc; }
  .slide-media .copy { position: absolute; left: 202px; top: 72px; width: 102px; }
</style>
</head>
<body>

<!-- Letterhead -->
<section class="piece letterhead">
  <svg class="shape" viewBox="0 0 475 673" preserveAspectRatio="none" aria-hidden="true">
    <polygon points="0,0 475,0 475,30 0,8" fill="#1c1e27"/>
    <polygon points="0,645 475,667 475,673 0,673" fill="#1c1e27"/>
  </svg>
  <div class="wordmark on-light"><span class="dot"></span>Velorin</div>
  <ul class="contact-list">
    <li><svg viewBox="0 0 10 10"><path d="M2 1h2l1 2-1.2 1a6 6 0 0 0 2.2 2.2L7 5l2 1v2c0 .6-.5 1-1 1A8 8 0 0 1 1 2c0-.5.4-1 1-1z"/></svg>+44 0113 872 604</li>
    <li><svg viewBox="0 0 10 10"><rect x="2.5" y="0.5" width="5" height="9" rx="1"/></svg>+44 7630 218 977</li>
    <li><svg viewBox="0 0 10 10"><path d="M0 2h10v6H0z"/></svg>maren@velorinathletic.example</li>
    <li><svg viewBox="0 0 10 10"><circle cx="5" cy="5" r="4.5"/></svg>velorinathletic.example</li>
  </ul>
  <div class="rule"></div>
  <p class="address">Corran Lodge, 14 Mill Bank Road,<br>Stockport, SK4 9TW<br>Company number 40718362</p>
  <p class="date">DATE:3/5/2018</p>
  <p class="salutation">Dear, Mr________</p>
  <div class="body">
    <p>Lorem ipsum dolor sit amet, consectetur adipiscing elit, sed do eiusmod tempor incididunt ut labore et dolore magna aliqua. Est pellentesque elit ullamcorper dignissim cras.</p>
    <p>Lorem ipsum dolor sit amet, consectetur adipiscing elit, sed do eiusmod tempor incididunt ut labore et dolore magna aliqua. Pharetra et ultrices neque ornare aenean euismod. Nunc eget lorem dolor sed viverra ipsum nunc. Ac ut consequat semper viverra nam libero. Eget gravida cum sociis natoque. Pretium viverra suspendisse potenti nullam. In hendrerit gravida rutrum quisque non. Ultrices gravida dictum fusce ut placerat orci. Accumsan tortor posuere ac ut consequat semper viverra. Feugiat sed lectus vestibulum mattis.</p>
    <p>Lorem ipsum dolor sit amet, consectetur adipiscing elit, sed do eiusmod tempor incididunt ut labore et dolore magna aliqua. Non arcu risus quis varius quam quisque. Tincidunt eget nullam non nisi est sit amet. Tincidunt tortor aliquam nulla facilisi cras fermentum odio eu feugiat. Id leo in vitae turpis massa sed elementum tempus egestas.</p>
  </div>
  <p class="sender">From: Maren Solwick ( Director )</p>
  <div class="signature" role="img" aria-label="Handwritten signature"></div>
</section>

<!-- Business card, personal side -->
<section class="piece card card-front">
  <p class="name">Maren Solwick</p>
  <p class="role">Director</p>
  <ul class="col col-left">
    <li>+44 0113 872 604 <svg viewBox="0 0 10 10"><path d="M2 1h2l1 2-1.2 1a6 6 0 0 0 2.2 2.2L7 5l2 1v2c0 .6-.5 1-1 1A8 8 0 0 1 1 2c0-.5.4-1 1-1z"/></svg></li>
    <li>+44 7630 218 977 <svg viewBox="0 0 10 10"><rect x="2.5" y="0.5" width="5" height="9" rx="1"/></svg></li>
  </ul>
  <div class="divider"></div>
  <ul class="col col-right">
    <li><svg viewBox="0 0 10 10"><path d="M0 2h10v6H0z"/></svg> maren@velorinathletic.example</li>
    <li><svg viewBox="0 0 10 10"><circle cx="5" cy="5" r="4.5"/></svg> velorinathletic.example</li>
  </ul>
  <p class="card-address">Corran Lodge, 14 Mill Bank Road,<br>Stockport, SK4 9TW Company number 40718362</p>
</section>

<!-- Business card, brand side -->
<section class="piece card card-back">
  <div class="wordmark on-dark"><span class="dot"></span>Velorin</div>
</section>

<!-- Envelope, flap side -->
<section class="piece envelope-back">
  <svg class="shape" viewBox="0 0 500 249" aria-hidden="true">
    <polygon points="0,0 500,0 488,70 476,82 24,82 12,70" fill="#ffffff"/>
  </svg>
  <div class="wordmark on-light"><span class="dot"></span>Velorin</div>
</section>

<!-- Envelope, address side -->
<section class="piece envelope-front">
  <div class="window"></div>
  <div class="wordmark on-dark"><span class="dot"></span>Velorin</div>
  <ul class="return-address">
    <li>+44 0113 872 604</li>
    <li>+44 7630 218 977</li>
    <li>maren@velorinathletic.example</li>
    <li>velorinathletic.example</li>
    <li class="gap">Corran Lodge, 14 Mill Bank Road,</li>
    <li>Stockport, SK4 9TW</li>
    <li class="gap">Company number 40718362</li>
  </ul>
</section>

<!-- Slide: cover -->
<section class="piece slide slide-cover">
  <div class="stadium" role="img" aria-label="Photograph of a floodlit football stadium at night"></div>
  <div class="wordmark on-dark"><span class="dot"></span>Velorin</div>
</section>

<!-- Slide: chart -->
<section class="piece slide slide-chart">
  <svg class="shape" viewBox="0 0 329 246" aria-hidden="true">
    <polygon points="0,212 329,186 329,246 0,246" fill="#191b22"/>
    <polygon points="190,215 329,203 329,226" fill="#caaa72"/>
  </svg>
  <h2 class="slide-title">TITLE GOES HERE</h2>
  <div class="slide-rule"></div>
  <p class="copy fine">Our athletes receive tailored representation across contract talks, brand partnerships and long term career planning. We combine sports expertise with commercial insight to secure lasting value. Each client benefits from dedicated advisers, clear reporting and a trusted network of clubs, sponsors and media partners worldwide. Performance on the field deserves equal care off it.</p>
  <svg class="chart" viewBox="0 0 125 106" role="img" aria-label="Bar chart of values A to E">
    <g font-family="Josefin Sans, sans-serif" font-size="7" fill="#ffffff">
      <text x="2" y="14">5</text><text x="2" y="30">4</text><text x="2" y="46">3</text>
      <text x="2" y="62">2</text><text x="2" y="77">1</text><text x="2" y="93">0</text>
    </g>
    <line x1="19" y1="88" x2="122" y2="88" stroke="#caaa72" stroke-width=".8"/>
    <rect x="22" y="52" width="14" height="36" fill="#ffffff"/>
    <rect x="41" y="3" width="14" height="85" fill="#caaa72"/>
    <rect x="60" y="22" width="14" height="66" fill="#caaa72"/>
    <rect x="79" y="39" width="14" height="49" fill="#ffffff"/>
    <rect x="98" y="22" width="14" height="66" fill="#caaa72"/>
    <g font-family="Josefin Sans, sans-serif" font-size="7" fill="#caaa72" text-anchor="middle">
      <text x="29" y="103">A</text><text x="48" y="103">B</text><text x="67" y="103">C</text>
      <text x="86" y="103">D</text><text x="105" y="103">E</text>
    </g>
  </svg>
  <div class="wordmark on-dark slide-footer-mark"><span class="dot"></span>Velorin</div>
</section>

<!-- Slide: diagram -->
<section class="piece slide slide-venn">
  <svg class="shape" viewBox="0 0 329 246" aria-hidden="true">
    <polygon points="0,212 329,186 329,246 0,246" fill="#191b22"/>
    <polygon points="190,215 329,203 329,226" fill="#caaa72"/>
  </svg>
  <h2 class="slide-title" style="top:30px">TITLE GOES HERE</h2>
  <div class="slide-rule" style="top:61px"></div>
  <p class="note" style="left:25px;top:96px">Scouting and talent care, with clear goals set for every season.</p>
  <p class="note" style="left:25px;top:135px">Contract guidance from first offer to final signature and beyond.</p>
  <p class="note" style="left:224px;top:96px">Brand building through selected partners that suit each athlete.</p>
  <p class="note" style="left:224px;top:135px">Welfare support covering travel, media duties and life after sport.</p>
  <svg class="venn" viewBox="0 0 108 110" role="img" aria-label="Three overlapping circles A, B and C">
    <g fill="#caaa72" fill-opacity=".72">
      <circle cx="53" cy="36" r="28"/>
      <circle cx="30" cy="72" r="28"/>
      <circle cx="76" cy="72" r="28"/>
    </g>
    <g font-family="Josefin Sans, sans-serif" font-size="18" fill="#ffffff" text-anchor="middle">
      <text x="53" y="33">A</text><text x="30" y="80">B</text><text x="76" y="80">C</text>
    </g>
  </svg>
  <div class="wordmark on-dark slide-footer-mark"><span class="dot"></span>Velorin</div>
</section>

<!-- Slide: media -->
<section class="piece slide slide-media">
  <svg class="shape" viewBox="0 0 329 246" aria-hidden="true">
    <polygon points="0,212 329,186 329,246 0,246" fill="#191b22"/>
    <polygon points="190,215 329,203 329,226" fill="#caaa72"/>
  </svg>
  <h2 class="slide-title">TITLE GOES HERE</h2>
  <div class="slide-rule" style="top:50px"></div>
  <div class="frame"><div class="placeholder" role="img" aria-label="Insert picture placeholder"></div></div>
  <p class="copy fine">We guide professional athletes through every stage of their careers. From first contracts to retirement planning, our team provides honest advice, careful negotiation and steady support. We work closely with clubs, governing bodies and sponsors to open the right doors. Every plan is built around the person, their goals and their long term wellbeing, both in competition and beyond it.</p>
  <div class="wordmark on-dark slide-footer-mark"><span class="dot"></span>Velorin</div>
</section>

</body>
</html>
```